HLT Crown Business Card Design 2020

Our Manor Steward is looking for a business card that is clean and straight to the point but still looks high-end and attractive. We are a team comprised of management and field professionals focused on the high-end residential marketplace. We serve homeowners and trade professionals directly based out of the Metrowest/Boston area. We provide client services as well as construction/renovation services.
We are aiming for a black and white feel (white background and black text) and a matte finish with rounded edges.

We want to emphasis our vision of "Properties - Projects - Partners".
Dana Fellmore is the president of HLT

Please include the following areas we service: Boston/Cape/Newport
Please make sure to include Dana's mobile (555) 302 4187 & office number (555) 640 2913, email dana@ourmanorsteward.example and website www.ourmanorsteward.example

Colors

Designer to choose only greyscale colors for use in the design.

Requirements
Must have
• Include "Properties - Projects - Partners" in design

Include "After Hours Emergency Support # 1800 555 0142" with icon

```html
<!DOCTYPE html>
<html lang="en">
<head>
<meta charset="utf-8">
<title>HLT Crown Business Cards</title>
<link href="https://fonts.googleapis.com/css2?family=Open+Sans:wght@400;600;700&family=Oswald:wght@500;600&display=swap" rel="stylesheet">
<style>
  :root {
    --ink: #2d2d2d;
    --ink-deep: #1c1c1c;
    --paper: #ffffff;
    --muted: #b5b5b5;
    --band-end: #6b6b6b;
    --rule: #3a3a3a;
    --shadow: rgba(0,0,0,0.28);
  }
  * { box-sizing: border-box; margin: 0; padding: 0; }
  html, body { width: 1200px; height: 1077px; overflow: hidden; background: var(--paper); }
  body { position: relative; font-family: "Open Sans", sans-serif; color: var(--ink); }
  .icons { position: absolute; width: 0; height: 0; }

  .card {
    position: absolute; width: 522px; height: 298px;
    border-radius: 16px; overflow: hidden;
    background: var(--paper);
    box-shadow: 2px 4px 7px var(--shadow), 0 0 1px rgba(0,0,0,0.2);
  }
  .card--front { background: var(--ink); }

  .brand { position: absolute; left: 32px; top: 30px; display: flex; flex-direction: column; }
  .brand__mark { font-family: "Oswald", sans-serif; font-weight: 600; font-size: 68px; line-height: 1; letter-spacing: 1px; color: var(--ink); }
  .brand__name { margin-top: 8px; font-weight: 700; font-size: 11.5px; letter-spacing: 1.6px; color: var(--ink); }

  .brand--center { left: 0; right: 0; top: 38px; align-items: center; }
  .brand--center .brand__mark { font-size: 84px; }
  .brand--center .brand__name { font-size: 13px; letter-spacing: 2px; margin-top: 6px; }

  .front-mark { position: absolute; left: 0; right: 0; top: 78px; text-align: center;
    font-family: "Oswald", sans-serif; font-weight: 600; font-size: 118px; line-height: 1; color: var(--ink-deep); }
  .front-motto { position: absolute; left: 0; right: 0; top: 240px; text-align: center;
    color: var(--paper); font-size: 13.5px; letter-spacing: 1.6px; font-weight: 400; }
  .front-support { position: absolute; left: 0; right: 0; top: 266px; display: flex; justify-content: center; align-items: center; gap: 6px;
    color: var(--muted); font-size: 11px; letter-spacing: 0.6px; }
  .front-support svg { width: 11px; height: 11px; fill: var(--muted); }

  .person { position: absolute; right: 32px; top: 128px; text-align: right; }
  .person__name { font-family: "Oswald", sans-serif; font-weight: 500; font-size: 23px; line-height: 1.15; color: var(--ink); }
  .person__role { font-size: 13px; line-height: 1.4; color: var(--ink); }

  .rule { position: absolute; left: 32px; right: 32px; top: 182px; border: 0; border-top: 1.2px solid var(--rule); }

  .contact { position: absolute; left: 32px; top: 203px; list-style: none; font-size: 13px; line-height: 17.5px; }
  .contact li { display: flex; align-items: center; gap: 6px; }
  .contact svg { width: 11px; height: 11px; fill: var(--ink); flex: none; }
  .contact--office { top: 220px; }

  .areas { position: absolute; right: 32px; top: 238px; font-size: 13.5px; letter-spacing: 0.2px; color: var(--ink); }
  .areas__sep { color: var(--ink); margin: 0 6px; }

  .band { position: absolute; left: 0; right: 0; bottom: 0; height: 29px;
    background: linear-gradient(to right, var(--ink) 88%, var(--band-end) 100%);
    display: flex; align-items: center; justify-content: space-between; padding: 0 34px 0 32px; }
  .band__url { color: var(--paper); font-size: 12.5px; letter-spacing: 1.4px; }
  .band__mark { font-family: "Oswald", sans-serif; font-weight: 600; font-size: 24px; line-height: 1; color: var(--paper); }
</style>
</head>
<body>
<svg class="icons" aria-hidden="true">
  <symbol id="i-mobile" viewBox="0 0 12 12"><path d="M3 0h6a1 1 0 0 1 1 1v10a1 1 0 0 1-1 1H3a1 1 0 0 1-1-1V1a1 1 0 0 1 1-1zm.3 1.3v8.2h5.4V1.3zM6 10a.6.6 0 1 0 0 1.2A.6.6 0 0 0 6 10z"/></symbol>
  <symbol id="i-phone" viewBox="0 0 12 12"><path d="M2.4.6l1.9-.4 1.1 2.8-1.3 1a6.5 6.5 0 0 0 3.9 3.9l1-1.3 2.8 1.1-.4 1.9c-.1.6-.7 1-1.3.9C5 10.1 1.9 7 1.5 1.9c-.1-.6.3-1.2.9-1.3z"/></symbol>
  <symbol id="i-mail" viewBox="0 0 12 12"><path d="M.5 2h11v8H.5zm1.3 1.1L6 6.4l4.2-3.3zM1.5 3.9V9h9V3.9L6 7.5z"/></symbol>
</svg>

<!-- Front -->
<article class="card card--front" style="left:44px; top:44px;">
  <div class="front-mark">HLT</div>
  <p class="front-motto">PROPERTIES - PROJECTS - PARTNERS</p>
  <p class="front-support"><svg><use href="#i-phone"/></svg>After Hours Emergency Support # 1800 555 0142</p>
</article>

<!-- Dana -->
<article class="card" style="left:632px; top:44px;">
  <div class="brand"><span class="brand__mark">HLT</span><span class="brand__name">OUR MANOR STEWARD</span></div>
  <div class="person"><h2 class="person__name">DANA FELLMORE</h2><p class="person__role">President</p></div>
  <hr class="rule">
  <ul class="contact">
    <li><svg><use href="#i-mobile"/></svg>(555) 302 4187</li>
    <li><svg><use href="#i-phone"/></svg>(555) 640 2913</li>
    <li><svg><use href="#i-mail"/></svg>dana@ourmanorsteward.example</li>
  </ul>
  <p class="areas">BOSTON<span class="areas__sep">|</span>CAPE<span class="areas__sep">|</span>NEWPORT</p>
  <footer class="band"><span class="band__url">ourmanorsteward.example</span><span class="band__mark">HLT</span></footer>
</article>

<!-- Reid -->
<article class="card" style="left:44px; top:388px;">
  <div class="brand"><span class="brand__mark">HLT</span><span class="brand__name">OUR MANOR STEWARD</span></div>
  <div class="person"><h2 class="person__name">REID CALLOWAY</h2><p class="person__role">Vice President</p></div>
  <hr class="rule">
  <ul class="contact">
    <li><svg><use href="#i-mobile"/></svg>(555) 418 2270</li>
    <li><svg><use href="#i-phone"/></svg>(555) 640 2913</li>
    <li><svg><use href="#i-mail"/></svg>reid@hltboston.example</li>
  </ul>
  <p class="areas">BOSTON<span class="areas__sep">|</span>CAPE<span class="areas__sep">|</span>NEWPORT</p>
  <footer class="band"><span class="band__url">hltboston.example</span><span class="band__mark">HLT</span></footer>
</article>

<!-- Owen -->
<article class="card" style="left:632px; top:388px;">
  <div class="brand"><span class="brand__mark">HLT</span><span class="brand__name">OUR MANOR STEWARD</span></div>
  <div class="person"><h2 class="person__name">OWEN PRATT</h2><p class="person__role">Client Services</p></div>
  <hr class="rule">
  <ul class="contact">
    <li><svg><use href="#i-mobile"/></svg>(555) 731 0968</li>
    <li><svg><use href="#i-phone"/></svg>(555) 640 2913</li>
    <li><svg><use href="#i-mail"/></svg>owen@ourmanorsteward.example</li>
  </ul>
  <p class="areas">BOSTON<span class="areas__sep">|</span>CAPE<span class="areas__sep">|</span>NEWPORT</p>
  <footer class="band"><span class="band__url">ourmanorsteward.example</span><span class="band__mark">HLT</span></footer>
</article>

<!-- Lena -->
<article class="card" style="left:44px; top:736px;">
  <div class="brand"><span class="brand__mark">HLT</span><span class="brand__name">OUR MANOR STEWARD</span></div>
  <div class="person"><h2 class="person__name">LENA MARWICK</h2><p class="person__role">Client Services</p></div>
  <hr class="rule">
  <ul class="contact">
    <li><svg><use href="#i-mobile"/></svg>(555) 226 5819</li>
    <li><svg><use href="#i-phone"/></svg>(555) 640 2913</li>
    <li><svg><use href="#i-mail"/></svg>lena@ourmanorsteward.example</li>
  </ul>
  <p class="areas">BOSTON<span class="areas__sep">|</span>CAPE<span class="areas__sep">|</span>NEWPORT</p>
  <footer class="band"><span class="band__url">ourmanorsteward.example</span><span class="band__mark">HLT</span></footer>
</article>

<!-- Office -->
<article class="card" style="left:632px; top:736px;">
  <div class="brand brand--center"><span class="brand__mark">HLT</span><span class="brand__name">OUR MANOR STEWARD</span></div>
  <hr class="rule">
  <ul class="contact contact--office">
    <li><svg><use href="#i-phone"/></svg>(555) 640 2913</li>
    <li><svg><use href="#i-mail"/></svg>office@ourmanorsteward.example</li>
  </ul>
  <p class="areas">BOSTON<span class="areas__sep">|</span>CAPE<span class="areas__sep">|</span>NEWPORT</p>
  <footer class="band"><span class="band__url">ourmanorsteward.example</span><span class="band__mark">HLT</span></footer>
</article>
</body>
</html>
```